Animated GIF banner for mobile app

We need a GIF Banner designed that alternates between two different ads.

Details are;
Pixel Size (W X H) 300 X 250
Minimum DPI 72dpi
File Size 40kb
File Size (Rich Media) 150kb

Ad 1 Text:
Lost super? More than one super fund? Contact us

Ad 2 Text:
Time to review your home loan? Contact us

Target Market(s)

30-55 year olds

Industry/Entity Type

Financial Service

Font styles to use
Sans Serif

Colors
0555a3
3176b5
85abd2

```html
<!DOCTYPE html>
<html lang="en">
<head>
<meta charset="utf-8">
<title>Super &amp; Home Loan Banner Set</title>
<link rel="stylesheet" href="https://fonts.googleapis.com/css2?family=Montserrat:wght@700;900&display=swap">
<style>
  :root {
    --page-bg: #ececec;
    --accent-green: #86c80c;
    --headline-white: #ffffff;
    --button-face: #f4f4f4;
    --button-text: #4a4a4a;
    --board-dark: #1b1b24;
    --board-mid: #2a2a36;
    --room-dark: #1a120e;
    --room-mid: #3a2a20;
    --table-wood: #4a3422;
    --piggy-pink: #e9c3d2;
    --books-slate: #3a3f58;
    --house-cream: #e6d2bd;
    --ribbon-red: #a8262e;
  }
  * { margin: 0; padding: 0; box-sizing: border-box; }
  html, body { width: 1200px; height: 1200px; overflow: hidden; }
  body {
    background: var(--page-bg);
    font-family: "Montserrat", Arial, sans-serif;
    position: relative;
  }
  .banner {
    position: absolute;
    left: 294px;
    width: 614px;
    height: 512px;
    overflow: hidden;
  }
  .banner--super {
    top: 66px;
    background: radial-gradient(ellipse at 70% 20%, var(--board-mid), var(--board-dark) 70%);
  }
  .banner--loan {
    top: 658px;
    background:
      linear-gradient(180deg, transparent 60%, var(--table-wood) 100%),
      radial-gradient(ellipse at 40% 10%, var(--room-mid), var(--room-dark) 75%);
  }
  .photo {
    position: absolute;
    border-radius: 14px 0 0 0;
  }
  .photo--piggy {
    left: 424px; top: 186px; width: 190px; height: 326px;
    background: linear-gradient(180deg, var(--piggy-pink) 0%, #d9b4c4 55%, var(--books-slate) 100%);
    opacity: 0.9;
  }
  .photo--house {
    left: 384px; top: 210px; width: 230px; height: 288px;
    background: linear-gradient(160deg, var(--house-cream) 0%, #cfa58c 50%, var(--ribbon-red) 100%);
    opacity: 0.9;
  }
  .headline {
    position: absolute;
    left: 76px;
    font-weight: 900;
    text-transform: uppercase;
    letter-spacing: -1px;
  }
  .headline span { display: block; }
  .headline__big {
    color: var(--accent-green);
    font-size: 88px;
    line-height: 74px;
    letter-spacing: -3px;
  }
  .headline__small {
    color: var(--headline-white);
    font-size: 44px;
    line-height: 45px;
  }
  .banner--super .headline { top: 72px; }
  .banner--super .headline__small:nth-of-type(3) { margin-top: 6px; }
  .banner--loan .headline { top: 74px; }
  .banner--loan .headline__big:nth-of-type(4) { margin-top: 4px; }
  .cta {
    position: absolute;
    left: 78px; top: 382px;
    width: 248px; height: 56px;
    display: flex;
    box-shadow: 0 3px 0 rgba(0,0,0,0.35);
  }
  .cta__label {
    flex: 1;
    background: var(--button-face);
    color: var(--button-text);
    font-weight: 700;
    font-size: 19px;
    display: flex; align-items: center; justify-content: center;
  }
  .cta__icon {
    width: 61px;
    background: var(--accent-green);
    display: flex; align-items: center; justify-content: center;
  }
</style>
</head>
<body>

<section class="banner banner--super">
  <div class="photo photo--piggy" role="img" aria-label="Pink piggy bank wearing glasses standing on a stack of books"></div>
  <h2 class="headline">
    <span class="headline__big">Lost</span>
    <span class="headline__big">Super?</span>
    <span class="headline__small">More than</span>
    <span class="headline__small">one super</span>
    <span class="headline__small">fund?</span>
  </h2>
  <a class="cta">
    <span class="cta__label">CONTACT US</span>
    <span class="cta__icon">
      <svg width="30" height="28" viewBox="0 0 30 28"><path d="M3 3 L13 14 L3 25 M15 3 L25 14 L15 25" fill="none" stroke="#1a1a1a" stroke-width="5"/></svg>
    </span>
  </a>
</section>

<section class="banner banner--loan">
  <div class="photo photo--house" role="img" aria-label="Small wooden house model tied with a red tartan ribbon bow on a table"></div>
  <h2 class="headline">
    <span class="headline__small">Time to</span>
    <span class="headline__small">review</span>
    <span class="headline__small">your</span>
    <span class="headline__big">Home</span>
    <span class="headline__big">Loan?</span>
  </h2>
  <a class="cta">
    <span class="cta__label">CONTACT US</span>
    <span class="cta__icon">
      <svg width="30" height="28" viewBox="0 0 30 28"><path d="M3 3 L13 14 L3 25 M15 3 L25 14 L15 25" fill="none" stroke="#1a1a1a" stroke-width="5"/></svg>
    </span>
  </a>
</section>

</body>
</html>
```